Restaurant Business Card Template

I need a business card created in the same color scheme and style as the attached label. Preferably it'd be in a .ai format.

Industry/Entity Type

German Restaurant

Contact Information for Business Card

Dorine Pekko, Front of House Manager, 612.307.4419, dorine@brunhofstuberestaurant.example, info@brunhofstuberestaurant.example, 417 Tamble Ave., Lower Level, Leavenworth, WA 98751.

Requirements
Must have
• Matching fonts and colors.
Nice to have
• If not able to match secondary font, something similar.

```html
<!DOCTYPE html>
<html lang="en">
<head>
<meta charset="utf-8">
<title>Brunhof Stube Restaurant – Business Card</title>
<link rel="stylesheet" href="https://fonts.googleapis.com/css2?family=Oswald:wght@300;400&display=swap">
<style>
  :root {
    --backdrop: #5a5a5a;
    --card-cream: #f7efe0;
    --card-cream-light: #fbf7ef;
    --paper-tan: #ecdcbc;
    --diamond-blue: #a9c2d2;
    --ink: #1c1a17;
    --gold: #9a7a2c;
  }
  * { box-sizing: border-box; margin: 0; padding: 0; }
  html, body {
    width: 1200px;
    height: 1200px;
    overflow: hidden;
    background: var(--backdrop);
  }
  .card {
    position: absolute;
    left: 310px;
    top: 92px;
    width: 580px;
    height: 1016px;
    background: linear-gradient(180deg, var(--paper-tan) 0%, var(--card-cream) 45%, var(--card-cream-light) 100%);
    overflow: hidden;
    font-family: "Oswald", "Arial Narrow", sans-serif;
    color: var(--ink);
  }
  .card__pattern {
    position: absolute;
    left: 0;
    top: 0;
    width: 100%;
    height: 460px;
    background:
      linear-gradient(180deg, rgba(247,239,224,0) 0%, var(--card-cream) 100%),
      linear-gradient(90deg, var(--diamond-blue) 0%, rgba(169,194,210,0.55) 45%, rgba(236,220,188,0.7) 100%);
    opacity: 0.75;
  }
  .card__brand {
    position: absolute;
    left: 0;
    top: 170px;
    width: 100%;
    text-align: center;
    font-weight: 400;
    color: var(--ink);
    font-size: 54px;
    line-height: 1.15;
    letter-spacing: 1px;
  }
  .card__person {
    position: absolute;
    left: 80px;
    top: 620px;
    font-size: 24px;
    line-height: 32px;
  }
  .card__name { font-weight: 400; }
  .card__title { font-weight: 400; color: var(--gold); }
  .card__contact {
    position: absolute;
    left: 80px;
    top: 710px;
    font-weight: 400;
    font-size: 24px;
    line-height: 32px;
  }
  .card__address {
    position: absolute;
    left: 80px;
    top: 850px;
    font-weight: 400;
    font-size: 24px;
    line-height: 32px;
  }
  .card__address-label { color: var(--gold); }
</style>
</head>
<body>
  <main class="card">
    <div class="card__pattern" role="img" aria-label="Faded blue and white Bavarian diamond pattern across the top of the card"></div>

    <h1 class="card__brand">Brunhof Stube<br>Restaurant</h1>

    <section class="card__person">
      <p class="card__name">Dorine Pekko</p>
      <p class="card__title">Front of House Manager</p>
    </section>

    <section class="card__contact">
      <p>+612 - 307 - 4419</p>
      <p>dorine@brunhofstuberestaurant.example</p>
      <p>info@brunhofstuberestaurant.example</p>
    </section>

    <section class="card__address">
      <p class="card__address-label">Address:</p>
      <p>417 Tamble Ave. Lower Level</p>
      <p>Leavenworth. WA 98751</p>
    </section>
  </main>
</body>
</html>
```